Business Card Design for Madam Rosette's Soak Parlor

Name: Madam Rosette's Soak Parlor. Maker of bath bombs, bath salts.

Card details:

Dolores Vantick
1.702.555.0193
Silverpine Nevada
dvantick47@mailbrook.test

"Bath bombs, bath salts and more..."

Industry/Entity Type

Business

Contact Information for Business Card

A picture of an old-fashioned bathtub (with claw feet) filled with bath bombs.

Colors include: Lavender, Pink, Turquois, Light Blue. Can you make the overall design look old fashioned.

```html
<!DOCTYPE html>
<html lang="en">
<head>
<meta charset="utf-8">
<title>Madam Rosette's Soak Parlor – Business Card</title>
<link rel="stylesheet" href="https://fonts.googleapis.com/css2?family=Tinos&family=Kalam:wght@400&display=swap">
<style>
  :root {
    --page-bg: #eef0f4;
    --rose: #e0469a;
    --coral: #e8566c;
    --magenta: #b4206e;
    --plum: #c42a86;
    --wave: #d3367f;
    --white: #ffffff;
    --photo-cream: #e9dcc4;
    --photo-tub: #f2eeea;
    --photo-pink: #f1b9d2;
  }
  * { margin: 0; padding: 0; box-sizing: border-box; }
  html, body {
    width: 1200px;
    height: 840px;
    overflow: hidden;
    background: var(--page-bg);
  }
  .canvas {
    width: 1200px;
    height: 840px;
    display: flex;
    align-items: center;
    justify-content: center;
  }
  .business-card {
    position: relative;
    width: 1000px;
    height: 610px;
    overflow: hidden;
    box-shadow: 0 10px 30px rgba(40, 30, 60, 0.18);
  }
  .card-art { position: absolute; inset: 0; width: 100%; height: 100%; }
  .brand {
    position: absolute;
    right: 120px;
    top: 80px;
    color: var(--white);
    text-align: right;
  }
  .brand-name {
    font-family: "Tinos", serif;
    font-weight: 400;
    font-size: 46px;
    line-height: 1;
    letter-spacing: 0.5px;
    white-space: nowrap;
  }
  .brand-tagline {
    font-family: "Kalam", cursive;
    font-weight: 400;
    font-size: 21px;
    margin-top: 8px;
    letter-spacing: 1px;
  }
  .owner-name {
    position: absolute;
    right: 70px;
    top: 300px;
    font-family: "Tinos", serif;
    font-weight: 400;
    font-size: 50px;
    line-height: 1;
    color: var(--white);
    white-space: nowrap;
  }
  .contact-row {
    position: absolute;
    right: 70px;
    top: 430px;
    display: flex;
    gap: 38px;
    list-style: none;
    font-family: "Tinos", serif;
    font-size: 22px;
    color: var(--white);
    white-space: nowrap;
  }
</style>
</head>
<body>
<main class="canvas">
  <article class="business-card">
    <svg class="card-art" viewBox="0 0 1000 610" preserveAspectRatio="none" aria-hidden="true">
      <defs>
        <linearGradient id="photoTones" x1="0" y1="0" x2="1" y2="1">
          <stop offset="0" stop-color="var(--photo-cream)"/>
          <stop offset="0.45" stop-color="var(--photo-pink)"/>
          <stop offset="0.75" stop-color="var(--photo-tub)"/>
          <stop offset="1" stop-color="var(--photo-cream)"/>
        </linearGradient>
        <linearGradient id="bandTones" x1="0" y1="0" x2="1" y2="0">
          <stop offset="0" stop-color="var(--rose)"/>
          <stop offset="0.7" stop-color="var(--rose)"/>
          <stop offset="1" stop-color="var(--coral)"/>
        </linearGradient>
        <linearGradient id="lowerTones" x1="0" y1="1" x2="1" y2="0">
          <stop offset="0" stop-color="var(--magenta)"/>
          <stop offset="1" stop-color="var(--plum)"/>
        </linearGradient>
      </defs>
      <rect class="photo-area" width="1000" height="610" fill="url(#photoTones)" role="img" aria-label="Photo of an old-fashioned claw-foot bathtub filled with colourful bath bombs"/>
      <path class="top-band" d="M240,0 H1000 V250 C860,250 700,150 520,140 C400,135 300,130 170,150 Z" fill="url(#bandTones)"/>
      <path class="wave-stripe" d="M520,260 C700,230 860,180 1000,160 V330 L560,320 Z" fill="var(--wave)"/>
      <path class="lower-panel" d="M90,610 L560,230 C700,260 860,290 1000,270 V610 Z" fill="url(#lowerTones)"/>
      <path class="corner-accent" d="M0,610 L90,610 L200,520 L0,590 Z" fill="var(--rose)" opacity="0.9"/>
    </svg>

    <header class="brand">
      <h1 class="brand-name">Madam Rosette's Soak Parlor</h1>
      <p class="brand-tagline">Bath bombs, bath salts and more...</p>
    </header>

    <h2 class="owner-name">Dolores Vantick</h2>

    <ul class="contact-row">
      <li class="contact-phone">1.702.555.0193</li>
      <li class="contact-city">Silverpine Nevada</li>
      <li class="contact-email">dvantick47@mailbrook.test</li>
    </ul>
  </article>
</main>
</body>
</html>
```